Travel Blogger Business Card for roamquill.net

I need a two-sided business card for a travel blogging website. The card should be both professional and fun at the same time. This is for the website www.roamquill.net

I don't necessarily think that the current logo on the website needs to be used on the business card but it can be. I am very flexible with ideas

Target Market(s)

Travel agencies that will be met at a conference.

Industry/Entity Type

Travel

Contact Information for Business Card

Company Name: Roam Quill.net
Name: Bertrand Olesky
Voice: +1-(345)-402-7731
Address: Coral Reach Shore, Grand Cayman, Cayman Islands
Email: ceo@roamquill.net

Colors
0592cd
0355a3
3176b5
33a6d7
85cae6
85acd3

Requirements
Must have
• Website address and name should be bigger than address, phone number, and email.

```html
<!DOCTYPE html>
<html lang="en">
<head>
<meta charset="utf-8">
<title>Roam Quill.net Business Card</title>
<link rel="stylesheet" href="https://fonts.googleapis.com/css2?family=Open+Sans:wght@400;600;700;800&display=swap">
<style>
  :root {
    --card-blue: #0555a5;
    --ink-white: #ffffff;
    --backdrop: #ececec;
    --card-shadow: rgba(0, 0, 0, 0.18);
  }
  * { margin: 0; padding: 0; box-sizing: border-box; }
  html, body {
    width: 1200px;
    height: 900px;
    overflow: hidden;
    background: var(--backdrop);
    font-family: "Open Sans", Arial, sans-serif;
    color: var(--ink-white);
  }
  .canvas {
    position: relative;
    width: 1200px;
    height: 900px;
  }
  .card {
    position: absolute;
    top: 301px;
    width: 520px;
    height: 297px;
    background: var(--card-blue);
    box-shadow: 0 10px 24px var(--card-shadow);
  }
  .card--front { left: 50px; }
  .card--back { left: 630px; }

  .brand {
    position: absolute;
    display: flex;
    align-items: center;
    gap: 12px;
  }
  .brand__dot {
    width: 30px;
    height: 30px;
    border-radius: 50%;
    background: var(--ink-white);
  }
  .brand__name {
    font-weight: 800;
    font-size: 30px;
    letter-spacing: 0.5px;
    text-transform: uppercase;
    line-height: 1;
  }

  /* Front side */
  .holder-name {
    position: absolute;
    left: 52px;
    top: 34px;
    font-size: 15px;
    font-weight: 700;
    text-transform: uppercase;
    letter-spacing: 0.3px;
  }
  .contact-list {
    position: absolute;
    left: 36px;
    top: 90px;
    list-style: none;
    font-size: 13px;
    line-height: 22px;
  }
  .contact-list li {
    display: flex;
    align-items: center;
    gap: 8px;
  }
  .contact-list svg {
    width: 11px;
    height: 11px;
    fill: var(--ink-white);
    flex: none;
  }
  .card--front .brand {
    left: 250px;
    top: 150px;
  }
  .address {
    position: absolute;
    left: 36px;
    bottom: 30px;
    display: flex;
    align-items: center;
    gap: 8px;
    font-size: 13px;
  }
  .address svg { width: 11px; height: 11px; fill: var(--ink-white); }

  /* Back side */
  .card--back .brand {
    left: 110px;
    top: 100px;
  }
  .card--back .brand__name { font-size: 36px; }
  .website {
    position: absolute;
    left: 0;
    right: 0;
    top: 180px;
    text-align: center;
    font-size: 17px;
    font-weight: 700;
    letter-spacing: 0.6px;
  }
</style>
</head>
<body>
<main class="canvas">

  <section class="card card--front" aria-label="Business card front">
    <p class="holder-name">Bertrand Olesky</p>
    <ul class="contact-list">
      <li>
        <svg viewBox="0 0 12 12" aria-hidden="true"><path d="M2.4 0.6 4.2 2.6 3.3 4.2c0.7 1.6 1.9 2.8 3.5 3.5L8.4 6.8l2 1.8-0.9 2.6C5 10.9 1.1 7 0.8 1.5z"/></svg>
        +1-(345)-402-7731
      </li>
      <li>
        <svg viewBox="0 0 12 12" aria-hidden="true"><path d="M0.5 2h11v8h-11z M1.5 3v0.4l4.5 3 4.5-3V3z" fill-rule="evenodd"/></svg>
        ceo@roamquill.net
      </li>
      <li>
        <svg viewBox="0 0 12 12" aria-hidden="true"><circle cx="6" cy="6" r="5.5"/><path d="M1 6h10M6 0.5c-2.6 3-2.6 8 0 11M6 0.5c2.6 3 2.6 8 0 11" stroke="#0555a5" stroke-width="0.9" fill="none"/></svg>
        www.roamquill.net
      </li>
    </ul>
    <div class="brand">
      <span class="brand__dot" aria-hidden="true"></span>
      <span class="brand__name">Roam Quill</span>
    </div>
    <p class="address">
      <svg viewBox="0 0 12 12" aria-hidden="true"><path d="M6 0.5a4 4 0 0 0-4 4c0 3 4 7 4 7s4-4 4-7a4 4 0 0 0-4-4zm0 2.2a1.8 1.8 0 1 1 0 3.6 1.8 1.8 0 0 1 0-3.6z" fill-rule="evenodd"/></svg>
      Coral Reach Shore, Grand Cayman, Cayman Islands
    </p>
  </section>

  <section class="card card--back" aria-label="Business card back">
    <div class="brand">
      <span class="brand__dot" aria-hidden="true"></span>
      <span class="brand__name">Roam Quill</span>
    </div>
    <p class="website">WWW.ROAMQUILL.NET</p>
  </section>

</main>
</body>
</html>
```